Business Card for Bloom Vitality & Strength

Hi can you please design a business card with my logo and program logo (the new one I just sent) somewhere on it too maybe on the back? Needs to be eye catching and super cool.
Trudy Melcombe, Director
Master Personal Trainer & Nutrition Coach
0472 816 305
Www.bloomvitalitystrength.com.au
Insta (logo) bloom_vitality_strength #bloomyou7x72018

Target Market(s)

30+ women looking to change lifestyle to healthy mind body etc

Industry/Entity Type

Health And Wellness

Contact Information for Business Card

As above

Font styles to use
Sans Serif

Colors

Designer to choose colors to be used in the design.

Requirements
Must have
• Must super cool and edgy with a bit of cuteness

```html
<!DOCTYPE html>
<html lang="en">
<head>
<meta charset="utf-8">
<title>Bloom Vitality &amp; Strength – Business Card</title>
<link href="https://fonts.googleapis.com/css2?family=Open+Sans:wght@400;600;700&display=swap" rel="stylesheet">
<style>
  :root {
    --backdrop: #ece6e0;
    --brand-red: #e01f26;
    --brand-red-deep: #a9171c;
    --card-white: #ffffff;
    --ink: #111111;
  }
  html, body {
    margin: 0;
    padding: 0;
    overflow: hidden;
  }
  body {
    width: 1200px;
    height: 1000px;
    background: var(--backdrop);
    position: relative;
    font-family: "Open Sans", sans-serif;
  }
  .card {
    position: absolute;
    width: 536px;
    height: 452px;
  }
  .card svg.card-shape {
    position: absolute;
    inset: 0;
    width: 100%;
    height: 100%;
    filter: drop-shadow(0 4px 8px rgba(0,0,0,0.18));
  }
  .card-front { left: 487px; top: 95px; }
  .card-back  { left: 126px; top: 482px; }

  /* Front: brand name with one plain circle beside it */
  .front-brand {
    position: absolute;
    left: 0;
    right: 0;
    top: 148px;
    display: flex;
    align-items: center;
    justify-content: center;
    gap: 16px;
  }
  .front-brand .brand-dot {
    width: 30px;
    height: 30px;
    border-radius: 50%;
    background: var(--card-white);
    flex: none;
  }
  .front-brand .brand-name {
    color: var(--card-white);
    font-weight: 700;
    font-size: 36px;
    line-height: 44px;
    letter-spacing: 0.5px;
    text-align: left;
  }
  .front-brand .brand-name span { display: block; }

  /* Back: program name with one plain circle beside it */
  .program-name {
    position: absolute;
    left: 0;
    right: 0;
    top: 88px;
    display: flex;
    align-items: center;
    justify-content: center;
    gap: 10px;
  }
  .program-name .program-dot {
    width: 22px;
    height: 22px;
    border-radius: 50%;
    background: var(--brand-red);
  }
  .program-name .program-text {
    font-size: 27px;
    font-weight: 400;
    letter-spacing: 3px;
    color: var(--ink);
    line-height: 36px;
  }

  .contact {
    position: absolute;
    left: 0;
    right: 0;
    top: 178px;
    text-align: center;
    color: var(--ink);
  }
  .contact .person {
    color: var(--brand-red);
    font-size: 22px;
    font-weight: 600;
    letter-spacing: 0.5px;
    line-height: 28px;
  }
  .contact .role {
    font-size: 19.5px;
    line-height: 22px;
  }
  .contact .phone {
    font-size: 17px;
    line-height: 22px;
    margin-top: 9px;
  }
  .contact .web {
    font-size: 17px;
    line-height: 22px;
  }
  .contact .web .accent { color: var(--brand-red); }
  .contact .social-dot {
    width: 13px;
    height: 13px;
    border: 2px solid var(--brand-red);
    border-radius: 50%;
    margin: 16px auto 3px;
  }
  .contact .handle, .contact .tag {
    font-size: 17px;
    line-height: 23px;
  }
</style>
</head>
<body>

  <section class="card card-front" aria-label="Card front">
    <svg class="card-shape" viewBox="0 0 536 452" aria-hidden="true">
      <defs>
        <radialGradient id="frontGlow" cx="50%" cy="55%" r="60%">
          <stop offset="0%" stop-color="#e8222a"/>
          <stop offset="100%" stop-color="#a9171c"/>
        </radialGradient>
      </defs>
      <path d="M268 88 C232 18 120 -4 56 40 C-14 92 4 200 78 272 L268 452 L458 272 C532 200 550 92 480 40 C416 -4 304 18 268 88 Z" fill="url(#frontGlow)"/>
    </svg>
    <div class="front-brand">
      <span class="brand-dot"></span>
      <div class="brand-name">
        <span>BLOOM VITALITY</span>
        <span>&amp; STRENGTH</span>
      </div>
    </div>
  </section>

  <section class="card card-back" aria-label="Card back">
    <svg class="card-shape" viewBox="0 0 536 452" aria-hidden="true">
      <path d="M268 88 C232 18 120 -4 56 40 C-14 92 4 200 78 272 L268 452 L458 272 C532 200 550 92 480 40 C416 -4 304 18 268 88 Z" fill="var(--card-white)"/>
    </svg>

    <div class="program-name">
      <span class="program-dot"></span>
      <span class="program-text">BloomU7x7</span>
    </div>

    <div class="contact">
      <div class="person">TRUDY MELCOMBE</div>
      <div class="role">Master Personal Trainer &amp; Nutrition Coach</div>
      <div class="role">- Director -</div>
      <div class="phone">0472 816 305</div>
      <div class="web">www.<span class="accent">bloomvitalitystrength</span>.com.au</div>
      <div class="social-dot"></div>
      <div class="handle">bloom_vitality_strength</div>
      <div class="tag">#bloomyou7x72018</div>
    </div>
  </section>

</body>
</html>
```